NORTHVALE

Labels for Men's Skin Care. Organic, target 25-35 The label will be 2x3.5 on a 4oz amber bottle. 3 labels with the information shown on the uploaded sample.
Our product is a e-commerce built to help my 24 year old twin sons have a business of their own. Although it will be sold online they will also do foot work and sell to barbers at barber shops using as a mist on customers after shaving. So we want something that will attract male customers and will look good in a modern Barbershop. This is there shot and packaging is very very important. So if you could help us out with a great label we would be working with you in the future for package design. Our line will have several mens Organic natural skin care cleanser, mask toners and moisturizers..Thank you for your help. We also hope to put our products in beauty supply shops. So it needs to stand out as a mans product but still be traditional male product. Oh be creative mind that you are and remember we are trying to build a brand that attracts 25-35 male. Thank you

Hello, I just wanted to let you know that I am up working very late.

for anyone on the other side of the world up and working. I sleep about
3 hours.. So I'll be up for a few more hours and then up again around 5am my time

Good morning... I just wanted to say I will need three labels.. The words on all three are not that different and will fit pretty much the same on all three. So if you could work with one showing how the colors might be a little different on the other two you can do that with just the one label Just to make it easier on you if you like.. we can fix the other two once I find the right label,  Thank you it is 3am here.. still working.. I love it.

Target Market(s)

MALE 25-35

Industry/Entity Type

E-Commerce

Requirements
Must have
• final design must be fitted to the dieline uploaded.

```html
<!DOCTYPE html>
<html lang="en">
<head>
<meta charset="utf-8">
<title>Northvale – Barber Line Labels</title>
<link href="https://fonts.googleapis.com/css2?family=Macondo&family=Tinos&display=swap" rel="stylesheet">
<style>
  :root {
    --canvas-bg: #ffffff;
    --canvas-frame: #4a4a4a;
    --label-green: #dbe08b;
    --band-green: #cbd46c;
    --leaf-light: #c6d06a;
    --leaf-mid: #9ebf3e;
    --ink: #311e26;
  }
  * { box-sizing: border-box; margin: 0; padding: 0; }
  html, body { width: 1200px; height: 1000px; overflow: hidden; background: var(--canvas-bg); }
  .canvas {
    position: relative; width: 1200px; height: 1000px;
    border: 2px solid var(--canvas-frame); background: var(--canvas-bg);
  }
  .label {
    position: absolute; top: 258px; width: 339px; height: 594px;
    background: var(--label-green); overflow: hidden; color: var(--ink);
  }
  .label--shave { left: 24px; }
  .label--soothe { left: 430px; }
  .label--mist { left: 837px; }

  .range-name {
    position: absolute; left: 14px; top: 18px;
    font-family: "Macondo", cursive; font-size: 24px; font-weight: 400; color: var(--ink);
  }
  .tree-art {
    position: absolute; left: 198px; top: 8px; width: 132px; height: 96px;
    border-radius: 50% 50% 40% 40%;
    background: radial-gradient(ellipse at 50% 40%, var(--leaf-mid), var(--leaf-light) 70%, transparent 72%);
  }
  .brand-name {
    position: absolute; left: 0; right: 0; top: 104px; text-align: center;
    font-family: "Macondo", cursive; font-size: 44px; font-weight: 400;
    color: var(--ink); white-space: nowrap;
  }
  .ornament {
    position: absolute; left: 0; top: 170px; width: 339px; height: 336px;
    background:
      radial-gradient(ellipse 90px 120px at 20px 50px, rgba(198,208,106,.55), transparent 70%),
      radial-gradient(ellipse 110px 140px at 320px 280px, rgba(198,208,106,.5), transparent 70%);
  }
  .product-title {
    position: absolute; left: 0; right: 0; top: 218px; text-align: center;
    font-family: "Tinos", serif; font-size: 27px; font-weight: 400; white-space: nowrap;
  }
  .benefits {
    position: absolute; left: 0; right: 0; top: 290px; text-align: center;
    font-family: "Macondo", cursive; font-size: 24px; line-height: 41.7px; list-style: none;
  }
  .info-band {
    position: absolute; left: 0; bottom: 0; width: 100%; height: 88px;
    background: var(--band-green); font-family: "Tinos", serif;
  }
  .info-band .tagline { position: absolute; left: 0; right: 0; top: 12px; text-align: center; font-size: 21px; }
  .info-band .volume { position: absolute; left: 62px; top: 42px; font-size: 27px; }
</style>
</head>
<body>
<div class="canvas">
  <section class="label label--shave">
    <p class="range-name">Barber Line</p>
    <div class="tree-art" role="img" aria-label="Illustration of a leafy green tree"></div>
    <h1 class="brand-name">NORTHVALE</h1>
    <div class="ornament" role="img" aria-label="Faint floral swirl decoration"></div>
    <h2 class="product-title">Herbal Soothing Lotion</h2>
    <ul class="benefits"><li>Treat &amp; Prevent</li><li>Ingrown Hair +</li><li>Calms Razor Burn</li><li>After Shaving</li></ul>
    <div class="info-band"><p class="tagline">Organic Natural Healing</p><p class="volume">3.5 fl oz 103 ml</p></div>
  </section>

  <section class="label label--soothe">
    <p class="range-name">Barber Line</p>
    <div class="tree-art" role="img" aria-label="Illustration of a leafy green tree"></div>
    <h1 class="brand-name">NORTHVALE</h1>
    <div class="ornament" role="img" aria-label="Faint floral swirl decoration"></div>
    <h2 class="product-title">Herbal Soothing Lotion</h2>
    <ul class="benefits"><li>Maintain Groin</li><li>Freshness &amp; Dryness</li><li>While Reducing Skin</li><li>Irritation &amp; Chafing</li></ul>
    <div class="info-band"><p class="tagline">Cranberry + Pomogrenate</p><p class="volume">3.5 fl oz 103 ml</p></div>
  </section>

  <section class="label label--mist">
    <p class="range-name">Barber Line</p>
    <div class="tree-art" role="img" aria-label="Illustration of a leafy green tree"></div>
    <h1 class="brand-name">NORTHVALE</h1>
    <div class="ornament" role="img" aria-label="Faint floral swirl decoration"></div>
    <h2 class="product-title">Cool Comfort Mist</h2>
    <ul class="benefits"><li>Maintain Groin</li><li>Freshness &amp; Dryness</li><li>While Reducing Skin</li><li>Irritation &amp; Chafing</li></ul>
    <div class="info-band"><p class="tagline">Organic Natural Healing</p><p class="volume">3.5 fl oz 103 ml</p></div>
  </section>
</div>
</body>
</html>
```